Label Redesign For Hemp Oil Tincture Bottle*

I need a label redesigned for Marbleleaf Hemp, current bottle label and logo is attached. The current label doesn't standout, not sure if its the font size or colors on the existing label. It is very important to have on the label that this is a Premium Full Spectrum Hemp Oil that is 2000mg. Then after the label is redesigned and approved, I would need to packaging to be designed to match the approved label design.
This Hemp oil has a relaxing effect to help ease mental and emotional stress, tension and worry. The Omega Fatty Acids it contains also naturally improves your mood and overall brain function, causing you to feel more alert and focused. Hemp Oil helps with insomnia. Take some 2-3 hours before bedtime, you will feel relaxed yet aware of how tired you are that it will lead to a good night's sleep. Hemp Oil helps ease chronic pain and inflammation from conditions such as arthritis, fibromyalgia, lupus, and MS. As a pain relief supplement, it is a safer, natural, non-chemical and non-addictive alternative to prescription painkillers.

Target Market(s)

Adults

Industry/Entity Type

Supplement

Font styles to use
Serif
Sans Serif

Colors

Designer to choose colors to be used in the design.

Requirements
Must have
• All information thats on current label but where it says 750 in the front of the existing label, it needs to say 2000. The 2000 should be prominent on the label.

```html
<!DOCTYPE html>
<html lang="en">
<head>
<meta charset="utf-8">
<title>Marbleleaf Hemp – Tincture Label</title>
<link href="https://fonts.googleapis.com/css2?family=Playfair+Display:wght@400&family=Montserrat:wght@300;700&family=Tinos&family=Allura&display=swap" rel="stylesheet">
<style>
  :root {
    --backdrop: #e6f6ea;
    --label: #ffffff;
    --sage: #afc675;
    --ink: #5f5f5f;
    --ink-soft: #6d6d6d;
    --rule: #9a9a9a;
  }
  * { margin: 0; padding: 0; box-sizing: border-box; }
  html, body { width: 1002px; height: 1200px; overflow: hidden; }
  body { background: var(--backdrop); position: relative; }

  .label {
    position: absolute; left: 111px; top: 48px;
    width: 780px; height: 1104px;
    background: var(--label);
    box-shadow: 0 6px 24px rgba(0,0,0,0.08);
    overflow: hidden;
  }
  .brand-mark {
    position: absolute; left: 345px; top: 156px;
    width: 90px; height: 90px; border-radius: 50%;
    background: var(--sage);
  }
  .brand-name {
    position: absolute; left: 0; right: 0; top: 290px;
    text-align: center;
    font-family: "Playfair Display", serif; font-size: 54px;
    font-weight: 400; color: var(--ink); letter-spacing: 2px;
    white-space: nowrap;
  }
  .product-name {
    position: absolute; left: 0; right: 0; top: 382px;
    text-align: center;
    font-family: "Playfair Display", serif; font-size: 77px;
    font-weight: 400; color: var(--ink); letter-spacing: 3px; white-space: nowrap;
  }
  .spectrum-pill {
    position: absolute; left: 137px; top: 485px;
    width: 504px; height: 54px; border-radius: 27px;
    background: var(--sage); color: #fff;
    font-family: "Montserrat", sans-serif; font-weight: 700;
    font-size: 27px; letter-spacing: 2.5px;
    display: flex; align-items: center; justify-content: center;
  }
  .strength {
    position: absolute; left: 0; right: 0; top: 540px;
    text-align: center;
    font-family: "Montserrat", sans-serif; font-weight: 300;
    font-size: 47px; color: var(--ink); letter-spacing: 3px;
  }
  .strength strong { font-weight: 700; }

  .zigzag-rule { position: absolute; display: block; }
  .zigzag-rule.upper { left: 0; top: 706px; }
  .zigzag-rule.lower { left: 525px; top: 853px; }

  .flavor {
    position: absolute; left: 0; right: 0; top: 740px;
    text-align: center;
    font-family: "Allura", cursive; font-size: 66px; color: #222;
  }

  .benefits-panel {
    position: absolute; left: 0; top: 868px;
    width: 515px; height: 236px;
    background: var(--sage);
  }
  .benefits-panel::before {
    content: ""; position: absolute; left: 0; top: -10px;
    width: 525px; height: 10px;
    background:
      linear-gradient(-45deg, var(--sage) 5px, transparent 0),
      linear-gradient(45deg, var(--sage) 5px, transparent 0);
    background-size: 10px 10px;
    background-position: left bottom;
    background-repeat: repeat-x;
  }
  .benefits-panel::after {
    content: ""; position: absolute; right: -10px; top: 0;
    width: 10px; height: 236px;
    background:
      linear-gradient(45deg, var(--sage) 5px, transparent 0),
      linear-gradient(135deg, var(--sage) 5px, transparent 0);
    background-size: 10px 10px;
    background-position: left top;
    background-repeat: repeat-y;
  }
  .benefits {
    position: absolute; left: 90px; top: 36px;
    list-style: none;
    font-family: "Tinos", serif; font-size: 27px;
    color: #fff; letter-spacing: 2px; line-height: 39.5px;
  }
  .benefits li::before { content: "•"; margin-right: 16px; }

  .net-contents {
    position: absolute; left: 586px; top: 948px;
    font-family: "Tinos", serif; font-size: 17px;
    color: var(--ink-soft); line-height: 21px; letter-spacing: 0.5px;
  }
</style>
</head>
<body>
  <main class="label">
    <div class="brand-mark" aria-hidden="true"></div>
    <div class="brand-name">Hollowfern</div>
    <h1 class="product-name">Marbleleaf Hemp</h1>
    <div class="spectrum-pill">PREMIUM FULL SPECTRUM</div>
    <div class="strength"><strong>2000</strong> HEMP OIL</div>

    <svg class="zigzag-rule upper" width="780" height="10" aria-hidden="true">
      <defs>
        <pattern id="zigzag" width="10" height="10" patternUnits="userSpaceOnUse">
          <path d="M0 2 L5 7 L10 2" fill="none" stroke="#9a9a9a" stroke-width="1.2"/>
        </pattern>
      </defs>
      <rect width="780" height="10" fill="url(#zigzag)"/>
    </svg>

    <div class="flavor">Natural Peppermint Flavor</div>

    <svg class="zigzag-rule lower" width="255" height="10" aria-hidden="true">
      <rect width="255" height="10" fill="url(#zigzag)"/>
    </svg>

    <section class="benefits-panel">
      <ul class="benefits">
        <li>STRESS RELIEF</li>
        <li>ANTI-INFLAMMATORY</li>
        <li>GET BETTER SLEEP</li>
        <li>PURE &amp; ORGANIC</li>
      </ul>
    </section>

    <div class="net-contents">1FLOZ (30ML)<br>DIETARY<br>SUPPLEMENT</div>
  </main>
</body>
</html>
```